Velvet Afterhours Poster Design

Need poster design made up in next few days, can guarantee payment to winner. Poster must contain the following but feel free to word it better:
Velvet Afterhours
Presented by quendor Sounds
Select resident djs
Drink specials all night
Open from 8pm to 12pm
Find us on Friendsphere
At Marlow Suites every Saturday
These will be on posters and fliers
Of a3 and roughly a5 size.
Our target audience is people 18-25
We want the posters to be exciting and professional. We would like a blue or purple with black color scheme but there is plenty of room for creative license so have a play around with what you think looks good. We currently don't have a logo but if your including one we would like to see it as c6 as in carbon as an element. Our first drink special is cocktails in jars but is not essential to include, can provide proper copy of the picture if you want to include it in your design. Please contact us if you need more information. we will be quick to pick a winner so payment will be provided fast!!!
Thank you all in advance for your submissions!!

```html
<!DOCTYPE html>
<html lang="en">
<head>
<meta charset="utf-8">
<title>Velvet Afterhours – Poster</title>
<link rel="stylesheet" href="https://fonts.googleapis.com/css2?family=Comfortaa:wght@700&family=Josefin+Sans:wght@400&family=Oswald:wght@500&display=swap">
<style>
  :root{
    --page:#ffffff;
    --ink-black:#000000;
    --ink-night:#17151d;
    --violet-deep:#6a3494;
    --violet-mid:#7d55a8;
    --violet-soft:#9a7cc0;
    --paper:#f6f4f9;
    --white:#ffffff;
    --footer-ink:#6b3a96;
  }
  html,body{margin:0;padding:0;overflow:hidden;background:var(--page);}
  .canvas{position:relative;width:1200px;height:1000px;overflow:hidden;background:var(--page);}
  .poster-art{position:absolute;left:0;top:0;width:1200px;height:1000px;}
  .poster-shadow{filter:drop-shadow(0 1px 3px rgba(0,0,0,.35));}
  .title{font-family:'Comfortaa',sans-serif;font-weight:700;fill:var(--white);stroke:var(--white);stroke-width:3;stroke-linejoin:round;}
  .presenter{font-family:'Comfortaa',sans-serif;font-weight:700;fill:var(--white);stroke:var(--white);stroke-width:0.6;}
  .band-text{font-family:'Josefin Sans',sans-serif;font-weight:400;fill:var(--white);}
  .feature{font-family:'Oswald',sans-serif;font-weight:500;fill:var(--white);}
  .brand-name{font-family:'Oswald',sans-serif;font-weight:500;fill:var(--white);letter-spacing:1px;}
  .footer-text{font-family:'Josefin Sans',sans-serif;font-weight:400;fill:var(--footer-ink);}
</style>
</head>
<body>
<main class="canvas">
<svg class="poster-art" viewBox="0 0 1200 1000" width="1200" height="1000" xmlns="http://www.w3.org/2000/svg">
  <!-- poster sheet -->
  <g class="poster-shadow">
    <rect x="265" y="27" width="669" height="944" fill="var(--paper)"/>
  </g>
  <rect class="sheet-left" x="265" y="27" width="335" height="895" fill="var(--ink-black)"/>
  <rect class="sheet-right" x="600" y="27" width="334" height="895" fill="var(--ink-night)"/>

  <!-- header ribbons, left -->
  <g class="ribbon-left">
    <rect x="265" y="122" width="135" height="68" fill="var(--violet-deep)"/>
    <polygon points="290,190 400,190 358,208 265,208 265,190" fill="var(--violet-soft)"/>
    <rect x="265" y="208" width="93" height="64" fill="var(--violet-deep)"/>
    <polygon points="265,272 358,272 295,337 265,337" fill="var(--violet-soft)"/>
  </g>
  <!-- header ribbons, right -->
  <g class="ribbon-right">
    <rect x="800" y="122" width="134" height="68" fill="var(--violet-deep)"/>
    <polygon points="910,190 800,190 842,208 934,208 934,190" fill="var(--violet-soft)"/>
    <rect x="842" y="208" width="92" height="64" fill="var(--violet-deep)"/>
    <polygon points="934,272 842,272 905,337 934,337" fill="var(--violet-soft)"/>
  </g>

  <!-- drink illustrations as flat placeholders -->
  <rect x="273" y="70" width="38" height="50" fill="var(--violet-deep)" role="img" aria-label="Cocktail jar illustration"/>
  <rect x="325" y="84" width="28" height="36" fill="var(--violet-deep)" role="img" aria-label="Cocktail jar illustration"/>
  <rect x="878" y="70" width="38" height="50" fill="var(--violet-deep)" role="img" aria-label="Cocktail jar illustration"/>
  <rect x="845" y="855" width="44" height="62" fill="var(--violet-deep)" role="img" aria-label="Cocktail jar illustration"/>

  <!-- title -->
  <text class="title" x="428" y="180" font-size="70" textLength="344" lengthAdjust="spacingAndGlyphs">VELVET</text>
  <text class="title" x="392" y="266" font-size="64" textLength="416" lengthAdjust="spacingAndGlyphs">AFTERHOURS</text>
  <text class="presenter" x="433" y="308" font-size="18" textLength="332" lengthAdjust="spacingAndGlyphs">presented by quendor sounds</text>

  <!-- schedule band -->
  <rect class="schedule-band" x="265" y="337" width="669" height="26" fill="var(--violet-mid)"/>
  <text class="band-text" x="352" y="359" font-size="22" textLength="496" lengthAdjust="spacing">EVERY SATURDAY · 8 - 12PM</text>

  <!-- brand mark -->
  <circle cx="600" cy="423" r="20" fill="none" stroke="var(--white)" stroke-width="6"/>
  <text class="brand-name" x="600" y="474" font-size="18" text-anchor="middle">VELVET AFTERHOURS</text>

  <!-- chevron feature bands -->
  <g class="chevrons">
    <polygon points="265,452 600,548 600,658 265,562" fill="var(--violet-deep)"/>
    <polygon points="934,452 600,548 600,658 934,562" fill="var(--violet-mid)"/>
    <polygon points="265,602 600,697 600,783 265,688" fill="var(--violet-deep)"/>
    <polygon points="934,602 600,697 600,783 934,688" fill="var(--violet-mid)"/>
    <polygon points="265,730 600,826 600,888 265,792" fill="var(--violet-deep)"/>
    <polygon points="934,730 600,826 600,888 934,792" fill="var(--violet-mid)"/>
  </g>

  <g class="features">
    <text class="feature" transform="translate(432,556) rotate(16)" font-size="84" text-anchor="middle" dominant-baseline="central" textLength="240" lengthAdjust="spacingAndGlyphs">SELECT</text>
    <text class="feature" transform="translate(764,558) rotate(-16)" font-size="56" text-anchor="middle" dominant-baseline="central" textLength="318" lengthAdjust="spacingAndGlyphs">RESIDENT DJS</text>
    <text class="feature" transform="translate(434,692) rotate(16)" font-size="50" text-anchor="middle" dominant-baseline="central" textLength="322" lengthAdjust="spacingAndGlyphs">DRINK SPECIALS</text>
    <text class="feature" transform="translate(766,692) rotate(-16)" font-size="72" text-anchor="middle" dominant-baseline="central" textLength="286" lengthAdjust="spacingAndGlyphs">ALL NIGHT</text>
    <text class="feature" transform="translate(426,808) rotate(16)" font-size="44" text-anchor="middle" dominant-baseline="central" textLength="292" lengthAdjust="spacingAndGlyphs">AT MARLOW SUITES</text>
    <text class="feature" transform="translate(765,808) rotate(-16)" font-size="44" text-anchor="middle" dominant-baseline="central" textLength="320" lengthAdjust="spacingAndGlyphs">EVERY SATURDAY</text>
  </g>

  <!-- footer -->
  <rect class="footer" x="265" y="922" width="669" height="49" fill="var(--paper)"/>
  <text class="footer-text" x="376" y="957" font-size="24" textLength="405" lengthAdjust="spacingAndGlyphs">FIND US ON FRIENDSPHERE</text>
  <rect x="797" y="935" width="25" height="25" rx="3" fill="var(--violet-soft)"/>
</svg>
</main>
</body>
</html>
```